Need a clean & modern homepage for an education site + opportunity for longer term work

Thanks for viewing our project. We are excited about this new website and we hope that we might build a relationship with designers as we work on this project. I provided quite a few details and requirements to help you more quickly create a design that meets our needs.
Who we are:
We are a website that discusses the importance of college accreditation and provides a directory of college programs.
What we need:
A homepage that meets the below requirements and is inspired by the examples provided
Definition of accredited:
ac·cred·it·ed [uh-kred-i-tid] adj.
1. officially recognized as meeting the essential requirements, as of academic excellence: accredited schools.
2. provided with official credentials, as by a government: an accredited diplomatic representative.
3. accepted as authoritative: an accredited theory.
Overall look and feel for the homepage:
- Clean, simple and modern
- Limited (or zero) pictures
- Utilize color blocks with text
- A trend seems to be longer vertical length homepages with lots of whitespace. I generally like this trend as long as the page is not way to tall.
Inspirations: Sites that have a similar look and feel to what I need.
http://plinvar.org/
http://www.tumbrelstat.com/colleges/harrowgate-university/
http://quietmarble.org/
http://www.vellichorstaffing.com/
http://www.plonk.com/
http://sketches.zimvo.com/
Items to be included on the homepage. Details below on each item.
- Top navigation
- Logo: Please leave a blank area for a logo. The logo has not been designed.
- Simple graphic/color block at the top that highlights a definition of “Accredited” – the definition should be formatted like it is being copy/pasted from a dictionary.
- Space for a video and small (50 word) written description of the video. You can use placeholder text.
- One section with 3 Paragraphs of content (each paragraph around 100 words) with a header at the top. You can use placeholder text but please create the formatting. At the end of the 3 paragraphs please have a “Read More” Note this shouldn't be 3 separate paragraphs with three read mores - it is 3 paragraphs with one read more at the end.
- An area with the header “Search Colleges by State” that has anchor text links to all 50 states.
Top navigation:
- Home
- States – with a subnav dropdown that includes all 50 US states.
- Programs – with a subnav dropdown that includes program titles (list below)
- Degrees - with a subnav dropdown that includes 5 degree levels (list below)
- Accreditation – no subnav
- Rankings – no subnav
- Resources – no subnav
Footer
- Link to about us, privacy, and a copyright www.url.com
Programs List for sub navigation
Accounting
Art
Bible
Business
Criminal Justice
Design
Engineering
English
Law
LPN to RN
Management
Math
MBA
MPH
Medical Assisting
Military
Nursing
Occupational Therapy
Paralegal
Psychology
Pharmacy
RN to BSN
Radiology
Social Work
Sonography
Degrees list for sub navigation
Certificate
Associate
Bachelors
Masters
PhD
Thanks so much - looking forward to working with you!

```html
<!DOCTYPE html>
<html lang="en">
<head>
<meta charset="utf-8">
<title>Accredited Colleges – Home</title>
<link rel="stylesheet" href="https://fonts.googleapis.com/css2?family=Montserrat:wght@400;600;700&family=PT+Sans:wght@400;700&display=swap">
<style>
  :root {
    --teal-deep: #327380;
    --teal-dark: #235562;
    --teal-accent: #58a9b7;
    --teal-link: #5aaab8;
    --teal-tint: #c9e4e8;
    --footer-bg: #374650;
    --white: #ffffff;
  }
  * { margin: 0; padding: 0; box-sizing: border-box; }
  html, body { width: 1200px; height: 1000px; overflow: hidden; background: var(--white); }
  body { position: relative; font-family: "PT Sans", sans-serif; }

  .content-section {
    position: absolute; left: 0; top: 0; width: 1200px; height: 576px;
    background: var(--teal-deep); color: var(--white);
  }
  .content-title {
    position: absolute; left: 164px; top: 13px;
    font-family: "Montserrat", sans-serif; font-weight: 400; font-size: 22px; letter-spacing: 0.2px;
  }
  .content-body { position: absolute; left: 164px; top: 66px; width: 880px; }
  .content-body p {
    font-size: 14.9px; line-height: 22.7px; margin-bottom: 25px; letter-spacing: -0.15px;
  }
  .read-more {
    position: absolute; left: 875px; top: 485px; width: 164px; height: 42px;
    background: var(--teal-dark); color: var(--white); text-decoration: none;
    font-weight: 700; font-size: 12.5px; text-transform: uppercase;
    display: flex; align-items: center; justify-content: center; border-radius: 2px;
  }

  .states-section { position: absolute; left: 0; top: 576px; width: 1200px; height: 377px; }
  .states-ribbon { position: absolute; left: 164px; top: 34px; width: 367px; height: 36px; }
  .states-ribbon svg { position: absolute; left: 0; top: 0; }
  .states-ribbon h2 {
    position: absolute; left: 0; top: 0; width: 100%; height: 36px;
    display: flex; align-items: center; justify-content: center;
    font-family: "Montserrat", sans-serif; font-weight: 700; font-size: 13.5px;
    color: var(--white); letter-spacing: 0; word-spacing: 2px; padding-right: 6px;
  }
  .state-list { position: absolute; list-style: none; }
  .state-list li { height: 22.7px; line-height: 22.7px; position: relative; }
  .state-list a {
    position: relative; z-index: 1;
    font-family: "Montserrat", sans-serif; font-weight: 600; font-size: 14px;
    color: var(--teal-link); text-decoration: none; letter-spacing: 0.25px;
  }
  .state-list .is-active .state-tab { position: absolute; left: -4px; top: 1px; z-index: 0; }
  .col-1 { left: 186px; top: 96px; }
  .col-2 { left: 406px; top: 96px; }
  .col-3 { left: 568px; top: 96px; }
  .col-4 { left: 707px; top: 94px; }
  .col-5 { left: 933px; top: 98px; }

  .site-footer {
    position: absolute; left: 0; top: 953px; width: 1200px; height: 47px;
    background: var(--footer-bg); color: var(--white); font-size: 14.5px;
  }
  .copyright { position: absolute; left: 165px; top: 13px; white-space: pre; }
  .footer-links { position: absolute; right: 165px; top: 13px; }
  .footer-links a { color: var(--white); text-decoration: none; }
  .footer-links span { margin: 0 5px; }
</style>
</head>
<body>

<section class="content-section">
  <h1 class="content-title">Lorem ipsum dolor sit amet</h1>
  <div class="content-body">
    <p>Lorem ipsum dolor sit amet, consectetur adipiscing elit. Integer nec odio. Praesent libero. Sed cursus ante dapibus diam. Sed nisi. Nulla quism at nibh elementum imperdiet. Duis sagittis ipsum. Praesent mauris. Fusce nec tellus sed augue semper porta. Mauris massa. Vestibulinia arcui eget nulla. Class aptent taciti sociosqu ad litora torquent per conubia nostra, per inceptos himenaeos. Curabitur sodales ligula in libero. Sedignissim lacinia nunc. Curabitur tortor. Pellentesque nibh. Aenean quam. In scelerisque sem at dolor. Maecenas mattis. Sed convallis tristue sem. Proin ut ligula vel nunc egestas porttitor. Morbi lectus risus, iaculis vel, suscipit quis, luctu.</p>
    <p>Lorem ipsum dolor sit amet, consectetur adipiscing elit. Integer nec odio. Praesent libero. Sed cursus ante dapibus diam. Sed nisi. Nulla quism at nibh elementum imperdiet. Duis sagittis ipsum. Praesent mauris. Fusce nec tellus sed augue semper porta. Mauris massa. Vestibulinia arcui eget nulla. Class aptent taciti sociosqu ad litora torquent per conubia nostra, per inceptos himenaeos. Curabitur sodales ligula in libero. Sedignissim lacinia nunc. Curabitur tortor. Pellentesque nibh. Aenean quam. In scelerisque sem at dolor. Maecenas mattis. Sed convallis tristue sem. Proin ut ligula vel nunc egestas porttitor. Morbi lectus risus, iaculis vel, suscipit quis, luctu.</p>
    <p>Lorem ipsum dolor sit amet, consectetur adipiscing elit. Integer nec odio. Praesent libero. Sed cursus ante dapibus diam. Sed nisi. Nulla quism at nibh elementum imperdiet. Duis sagittis ipsum. Praesent mauris. Fusce nec tellus sed augue semper porta. Mauris massa. Vestibulinia arcui eget nulla. Class aptent taciti sociosqu ad litora torquent per conubia nostra, per inceptos himenaeos. Curabitur sodales ligula in libero. Sedignissim lacinia nunc. Curabitur tortor. Pellentesque nibh. Aenean quam. In scelerisque sem at dolor. Maecenas mattis. Sed convallis tristue sem. Proin ut ligula vel nunc egestas porttitor. Morbi lectus risus, iaculis vel, suscipit quis, luctu.</p>
  </div>
  <a class="read-more" href="#">Read More</a>
</section>

<section class="states-section">
  <div class="states-ribbon">
    <svg width="367" height="36" viewBox="0 0 367 36" aria-hidden="true">
      <polygon points="18,0 349,0 367,18 349,36 18,36 0,18" fill="var(--teal-accent)"/>
    </svg>
    <h2>CHOOSE A COLLEGE BY STATE</h2>
  </div>

  <ul class="state-list col-1">
    <li class="is-active">
      <svg class="state-tab" width="134" height="21" viewBox="0 0 134 21" aria-hidden="true"><polygon points="0,0 123,0 134,10.5 123,21 0,21" fill="var(--teal-tint)"/></svg>
      <a href="#">Alabama</a>
    </li>
    <li><a href="#">Alaska</a></li>
    <li><a href="#">American Samoa</a></li>
    <li><a href="#">Arizona</a></li>
    <li><a href="#">Arkansas</a></li>
    <li><a href="#">California</a></li>
    <li><a href="#">Colorado</a></li>
    <li><a href="#">Connecticut</a></li>
    <li><a href="#">Delaware</a></li>
    <li><a href="#">District of Columbia</a></li>
  </ul>
  <ul class="state-list col-2">
    <li><a href="#">Florida</a></li>
    <li><a href="#">Georgia</a></li>
    <li><a href="#">Guam</a></li>
    <li><a href="#">Hawaii</a></li>
    <li><a href="#">Idaho</a></li>
    <li><a href="#">Illinois</a></li>
    <li><a href="#">Indiana</a></li>
    <li><a href="#">Iowa</a></li>
    <li><a href="#">Kansas</a></li>
    <li><a href="#">Kentucky</a></li>
  </ul>
  <ul class="state-list col-3">
    <li><a href="#">Louisiana</a></li>
    <li><a href="#">Maine</a></li>
    <li><a href="#">Maryland</a></li>
    <li><a href="#">Massachusetts</a></li>
    <li><a href="#">Michigan</a></li>
    <li><a href="#">Minnesota</a></li>
    <li><a href="#">Mississippi</a></li>
    <li><a href="#">Missouri</a></li>
    <li><a href="#">Montana</a></li>
    <li><a href="#">Nebraska</a></li>
  </ul>
  <ul class="state-list col-4">
    <li><a href="#">Nevada</a></li>
    <li><a href="#">New Hampshire</a></li>
    <li><a href="#">New Jersey</a></li>
    <li><a href="#">New Mexico</a></li>
    <li><a href="#">New York</a></li>
    <li><a href="#">North Carolina</a></li>
    <li><a href="#">North Dakota</a></li>
    <li><a href="#">Northern Marianas Islands</a></li>
    <li><a href="#">Ohio</a></li>
    <li><a href="#">Oklahoma</a></li>
  </ul>
  <ul class="state-list col-5">
    <li><a href="#">Oregon</a></li>
    <li><a href="#">Pennsylvania</a></li>
    <li><a href="#">Puerto Rico</a></li>
    <li><a href="#">Rhode Island</a></li>
    <li><a href="#">South Carolina</a></li>
    <li><a href="#">South Dakota</a></li>
    <li><a href="#">Tennessee</a></li>
    <li><a href="#">Texas</a></li>
    <li><a href="#">Utah</a></li>
    <li><a href="#">Vermont</a></li>
  </ul>
</section>

<footer class="site-footer">
  <p class="copyright">Copyright ©  2013  -  All Right Reserved</p>
  <nav class="footer-links">
    <a href="#">About us</a><span>|</span><a href="#">Privacy Information</a><span>|</span><a href="#">Site Map</a>
  </nav>
</footer>

</body>
</html>
```